We are a music event management company based out of Syracuse, NY but we do business in multiple areas like the mid-west and Florida.

Our primary events revolve around the Electronic Dance Music scene. (acts like Brinmoor, Nordic Loft Syndicate, Dorian Pell)

We would like a clean cut business card with Voltaramble written on the back. In Voltaramble we would like the u to be shaped like a sixteenth note. The colors green and silver would be nice to see somehow but not necessary. Feel free to play around with it and have fun because that's what our business is about, Having Fun!

Some similar examples for reference would be the Neon Orchard or Glowing Tulip Jamboree website.

Our goal is to provide people with an experience, not just a concert. There is a difference.

Reason: Needed more time to decide.

Industry/Entity Type

Events

```html
<!DOCTYPE html>
<html lang="en">
<head>
<meta charset="utf-8">
<title>Voltaramble — Business Card</title>
<link rel="stylesheet" href="https://fonts.googleapis.com/css2?family=Play:wght@700&display=swap">
<style>
  :root {
    --page-bg: #ffffff;
    --card-black: #000000;
    --card-sheen: #666666;
    --mesh-tone: #242424;
    --edge-grey: #3a3a3a;
    --green-deep: #566f00;
    --green-mid: #9cc92e;
    --green-glow: #f0ffb0;
    --green-bright: #dcff00;
    --silver: #d6d6d6;
  }
  html, body {
    margin: 0;
    padding: 0;
    width: 1200px;
    height: 1000px;
    overflow: hidden;
    background: var(--page-bg);
  }
  .canvas {
    position: relative;
    width: 1200px;
    height: 1000px;
  }
  .card-art {
    position: absolute;
    inset: 0;
    width: 1200px;
    height: 1000px;
  }
  .brand-name {
    font-family: "Play", sans-serif;
    font-weight: 700;
    font-size: 118px;
    fill: var(--silver);
  }
</style>
</head>
<body>
<main class="canvas">
  <svg class="card-art" viewBox="0 0 1200 1000" xmlns="http://www.w3.org/2000/svg">
    <defs>
      <linearGradient id="card-sheen" x1="115" y1="0" x2="1085" y2="0" gradientUnits="userSpaceOnUse">
        <stop offset="0" stop-color="var(--card-black)"/>
        <stop offset="0.55" stop-color="var(--card-sheen)"/>
        <stop offset="1" stop-color="var(--card-black)"/>
      </linearGradient>
      <linearGradient id="band-green" x1="115" y1="0" x2="1085" y2="0" gradientUnits="userSpaceOnUse">
        <stop offset="0" stop-color="var(--green-deep)"/>
        <stop offset="0.45" stop-color="var(--green-mid)"/>
        <stop offset="0.58" stop-color="var(--green-glow)"/>
        <stop offset="0.66" stop-color="var(--green-mid)"/>
        <stop offset="1" stop-color="var(--green-bright)"/>
      </linearGradient>
    </defs>

    <!-- card base -->
    <rect class="card-base" x="115" y="222" width="970" height="555" fill="url(#card-sheen)"/>

    <!-- mesh areas -->
    <path class="mesh-top" role="img" aria-label="Dark hexagon mesh texture"
          d="M115 222 H800 C740 270 690 318 590 318 H115 Z" fill="var(--mesh-tone)"/>
    <path class="mesh-bottom" role="img" aria-label="Dark hexagon mesh texture"
          d="M115 777 H800 C740 729 690 681 590 681 H115 Z" fill="var(--mesh-tone)"/>

    <!-- grey edge above swoosh -->
    <path class="swoosh-edge" d="M590 318 C690 318 740 270 800 222 H830 C760 272 700 337 590 337 Z" fill="var(--edge-grey)"/>
    <path class="swoosh-edge" d="M590 681 C690 681 740 729 800 777 H830 C760 727 700 662 590 662 Z" fill="var(--edge-grey)"/>

    <!-- green swoosh bands -->
    <path class="band band-top"
          d="M115 337 H590 C700 337 760 272 830 222 H1085 V242 L790 355 C740 375 700 392 640 392 H115 Z"
          fill="url(#band-green)"/>
    <path class="band band-bottom"
          d="M115 662 H590 C700 662 760 727 830 777 H1085 V757 L790 644 C740 624 700 607 640 607 H115 Z"
          fill="url(#band-green)"/>

    <!-- brand name -->
    <text class="brand-name" x="548" y="527" text-anchor="middle" textLength="600" lengthAdjust="spacingAndGlyphs">Voltaramble</text>
  </svg>
</main>
</body>
</html>
```